Global Harbor Learning Network

Our company needs a simple effective website with a clean design. We are working towards lowering the number of drownings that effect huge numbers each year. We will primarily link members to find education seminars, conferences and online material. With a forum to pose questions, have them answered by the community and moderated by staff members.

Target Market(s)

Swimming School Owners, Coaches, Parents and Community Groups

Industry/Entity Type

Education

Number of Pages Required

5+ page

Requirements
Must have
• A layout for all of the included pages. A good design for the forum. I will need to send this concept design to a coder for the final product.
Nice to have
• i would like to see an Olympic Swimming Pool incorporated into the options menu.

```html
<!DOCTYPE html>
<html lang="en">
<head>
<meta charset="utf-8">
<title>Global Harbor Learning Network</title>
<link href="https://fonts.googleapis.com/css2?family=Raleway:wght@400;500&family=Open+Sans:wght@400&display=swap" rel="stylesheet">
<style>
:root{
  --blue:#1a87e0;
  --blue-light:#41b2f3;
  --nav-top:#3aa2ee;
  --nav-bottom:#1479d2;
  --ink:#444;
  --muted:#777;
  --accent:#1e9be0;
  --footer:#e6e6e6;
  --white:#fff;
}
*{margin:0;padding:0;box-sizing:border-box}
html,body{width:735px;height:1200px;overflow:hidden;background:var(--white)}
body{position:relative;font-family:'Raleway',sans-serif;color:var(--ink)}
h1,h2,h3{font-weight:400}
.abs{position:absolute}
.topbar{left:0;top:0;width:735px;height:45px;background:var(--white)}
.login{left:593px;top:15px;width:60px;height:22px;border:1.5px solid var(--blue);color:var(--blue);font-size:8.5px;display:flex;align-items:center;justify-content:center}
.navband{left:0;top:45px;width:735px;height:35px;background:linear-gradient(var(--nav-top),var(--nav-bottom));z-index:2}
.nav{top:45px;height:35px;display:flex;align-items:center;gap:14px;color:var(--white);font-size:10px;z-index:3}
.nav.left{left:97px}
.nav.right{left:451px}
.brand{left:320px;top:6px;width:112px;height:112px;border-radius:50%;background:var(--white);box-shadow:0 1px 4px rgba(0,0,0,.25);z-index:4;display:flex;align-items:center;justify-content:center;text-align:center;color:var(--blue);font-size:11px;font-weight:500;line-height:1.25;padding:14px}
.hero{left:0;top:80px;width:735px;height:322px;background:linear-gradient(160deg,#1f8fbf,#4cb8d8 45%,#1a7eb0);z-index:1}
.hero-text{left:0;top:185px;width:735px;text-align:center;color:var(--white);z-index:2}
.hero-title{font-size:29px}
.hero-sub{font-size:19px;margin-top:5px}
.dots{left:342px;top:368px;display:flex;gap:3px;z-index:2}
.dots span{width:11px;height:11px;border-radius:50%;background:var(--white)}
.dots span:first-child{background:none;border:1.5px solid var(--white)}
.wave{left:0;top:360px;z-index:2}
.welcome-title{left:93px;top:433px;font-size:19.5px;line-height:1.2;color:#4a4a4a}
.welcome-title em{font-style:normal;color:var(--accent)}
.welcome-copy{left:93px;top:488px;width:375px;font-family:'Open Sans',sans-serif;font-size:7.3px;line-height:12.3px;color:var(--muted)}
.btn-more{left:93px;top:570px;width:75px;height:23px;border:1.5px solid var(--blue);color:var(--blue);font-size:8px;display:flex;align-items:center;justify-content:center}
.globe-art{left:494px;top:418px;width:130px;height:184px;background:radial-gradient(ellipse at 50% 60%,#2f7fd0 0%,#7fb6e8 45%,rgba(255,255,255,0) 72%)}
.card{top:634px;width:284px;height:221px}
.card.involved{left:81px}
.card.certified{left:370px}
.card-photo{height:128px}
.involved .card-photo{background:linear-gradient(135deg,#1a4fb0,#3b73cf)}
.certified .card-photo{background:linear-gradient(135deg,#5d7fa6,#8aa3bd)}
.card-body{height:93px;color:var(--white);text-align:center;padding:10px 16px 0}
.involved .card-body{background:var(--blue)}
.certified .card-body{background:var(--blue-light)}
.card-title{font-size:14px}
.card-text{font-family:'Open Sans',sans-serif;font-size:7.4px;line-height:12.3px;margin-top:5px}
.community-photo{left:97px;top:880px}
.community-title{left:322px;top:888px;font-size:18px;color:#222}
.member{left:326px;display:flex;gap:8px}
.member svg{margin-top:2px}
.member-place{font-size:8.5px;color:#444}
.member-role{font-family:'Open Sans',sans-serif;font-size:7.2px;color:var(--muted);margin-top:3px}
.footer{left:0;top:1123px;width:735px;height:77px;background:var(--footer)}
.footer-links{left:86px;top:1144px;display:flex;gap:13px;font-size:8.5px;color:#555}
.copyright{left:86px;top:1165px;font-family:'Open Sans',sans-serif;font-size:6.8px;color:#666}
.social{left:567px;top:1140px;display:flex;gap:3px}
.social span{width:18px;height:18px;border-radius:50%;border:1.3px solid #555}
</style>
</head>
<body>
<div class="abs topbar"></div>
<div class="abs login">LOG IN</div>
<div class="abs navband"></div>
<nav class="abs nav left"><span>About Us</span><span>Community</span><span>Why get Involved</span></nav>
<nav class="abs nav right"><span>Events</span><span>Become Certified</span><span>Contact</span></nav>
<div class="abs brand">Global Harbor Learning Network</div>

<div class="abs hero" role="img" aria-label="Photo of a child splashing in a swimming pool"></div>
<div class="abs hero-text">
  <h1 class="hero-title">Global Harbor Learning Network</h1>
  <p class="hero-sub">Providing Water Safety Education</p>
</div>
<div class="abs dots"><span></span><span></span><span></span><span></span></div>
<svg class="abs wave" width="735" height="45" viewBox="0 0 735 45">
  <path d="M0 20 Q180 -5 370 18 T735 22 V45 H0Z" fill="#c7e0ec"/>
  <path d="M0 24 Q180 5 370 24 T735 30 V45 H0Z" fill="#fff"/>
</svg>

<h2 class="abs welcome-title">WELCOME TO <em>GLOBAL HARBOR</em><br><em>LEARNING NETWORK</em></h2>
<p class="abs welcome-copy">Each year globally there are 372000 people drowning, from young children to victims of flood. According to a 2007 report released by Child Water Watch, as many as 30,000 children between 0 and 14 years old die by drowning each year in China. That accounts for up to 60 percent of China's annual 50,000 accidental child deaths and the falls and climbing? If this tally isn't frightening enough think of the non drownings that lead to permanent brain damage and disability. Spreading the message of water safety and education is important to reduce this number and give everyone a fighting chance.</p>
<div class="abs btn-more">READ MORE</div>
<div class="abs globe-art" role="img" aria-label="Illustration of a water drop holding a globe"></div>

<section class="abs card involved">
  <div class="card-photo" role="img" aria-label="Photo of a mother and baby swimming underwater"></div>
  <div class="card-body">
    <h3 class="card-title">Why become Involved</h3>
    <p class="card-text">The Best way to provide education is in a safe controlled environment. Running your own facility is a rewarding lifelong move into business. Providing a community service with an opportunity to work with a passionate and driven community.</p>
  </div>
</section>
<section class="abs card certified">
  <div class="card-photo" role="img" aria-label="Photo of a girl learning to swim in a pool"></div>
  <div class="card-body">
    <h3 class="card-title">Become Certified</h3>
    <p class="card-text">The Best way to provide education is in a safe controlled environment. Running your own facility is a rewarding lifelong move into business. Providing a community service with an opportunity to work with a passionate and driven community.</p>
  </div>
</section>

<svg class="abs community-photo" width="200" height="200" viewBox="0 0 200 200">
  <defs><linearGradient id="sea" x1="0" y1="0" x2="0" y2="1"><stop offset="0" stop-color="#4aa8a8"/><stop offset="1" stop-color="#2f7f86"/></linearGradient></defs>
  <path d="M22.5 40 A98 98 0 0 1 177.5 40" fill="none" stroke="#1a87e0" stroke-width="2"/>
  <path d="M29.4 168 A98 98 0 0 0 170.6 168" fill="none" stroke="#1a87e0" stroke-width="2"/>
  <circle cx="100" cy="100" r="88" fill="url(#sea)" role="img" aria-label="Photo of children wading into the sea"/>
</svg>
<h2 class="abs community-title">Our Community</h2>
<div class="abs member" style="top:924px">
  <svg width="16" height="18" viewBox="0 0 16 18"><path d="M8 1 C3 1 1 5 3 9 L8 17 L9 10 C14 9 14 1 8 1Z" fill="#1a87e0"/></svg>
  <div><div class="member-place">Australia</div><div class="member-role">Lena Whitcombe: Principal of Aquatic Education, GH China and owner of Bayview Swim School</div></div>
</div>
<div class="abs member" style="top:962px">
  <svg width="16" height="18" viewBox="0 0 16 18"><path d="M8 1 C3 1 1 5 3 9 L8 17 L9 10 C14 9 14 1 8 1Z" fill="#1a87e0"/></svg>
  <div><div class="member-place">China</div><div class="member-role">Mia Tanford: Founder and CEO of Ripple Swim School's 6 soon to be 7 locations.</div></div>
</div>
<div class="abs member" style="top:1000px">
  <svg width="16" height="18" viewBox="0 0 16 18"><path d="M8 1 C3 1 1 5 3 9 L8 17 L9 10 C14 9 14 1 8 1Z" fill="#1a87e0"/></svg>
  <div><div class="member-place">Hong Kong</div><div class="member-role">Owen Leung: Founder and CEO of Clearwater Swimming</div></div>
</div>
<div class="abs member" style="top:1038px">
  <svg width="16" height="18" viewBox="0 0 16 18"><path d="M8 1 C3 1 1 5 3 9 L8 17 L9 10 C14 9 14 1 8 1Z" fill="#1a87e0"/></svg>
  <div><div class="member-place">Canada</div><div class="member-role">Dana Whitlock: Founder of Lakeside Swim Centre USA</div></div>
</div>

<footer class="abs footer"></footer>
<nav class="abs footer-links"><span>About Us</span><span>Community</span><span>Why get Involved</span><span>Events</span><span>Become Certified</span><span>Contact</span></nav>
<p class="abs copyright">© 2016 Company Name &nbsp;All right reserved &nbsp;Term of Use</p>
<div class="abs social"><span></span><span></span><span></span><span></span></div>
</body>
</html>
```